Design a menu for health restaurant

A health food restaurant in Los Angeles is seeking menu design. Our foods are made from scratch using whole ingredients.
Name: Grubb Larder
Address: 1000 E 60th StLos Angeles, CA 90247
Website: www.GrubbLarder.example
We are looking for a clean and simple menu. Brand colors are white/tan, green and orange.

Please see attached excel with menu items and logo. We do not yet have prices.

Colors
f78f20
9bcb3c
ffffff
fff3d1

Requirements
Must have
• Easy to read.
Trifold menu design (front and back).
VEGAN, VEGETARIAN, GLUTEN FREE, CONTAINS NUTS symbols.
Logo.
Nice to have
• Incorporate brand colors, but still be easy to read.
We would like to use the Belco font (attached) if it works. If not we are open to a similar font that is easy to read.

Please see attached images.
We like the images and headers of OPTION 1. Would like something similar in trifold format.
We like the clean fonts of OPTION 2.

```html
<!DOCTYPE html>
<html lang="en">
<head>
<meta charset="utf-8">
<title>Grubb Larder – Menu Inside Spread</title>
<link rel="stylesheet" href="https://fonts.googleapis.com/css2?family=Archivo:wght@400;600;700&family=Yellowtail&family=Arimo:wght@700&display=swap">
<style>
  :root{
    --orange:#f78f20;
    --green:#9bcb3c;
    --white:#ffffff;
    --tan:#fff3d1;
    --ink:#1d1d1b;
    --body:#2b2b2b;
    --frame:#3a3a3a;
    --note:#9a9a9a;
  }
  *{box-sizing:border-box;margin:0;padding:0}
  html,body{width:1200px;height:1178px;overflow:hidden;background:var(--white)}
  body{position:relative;font-family:"Archivo",Arial,sans-serif;color:var(--ink)}

  .spread{position:absolute;left:71px;top:93px;width:1029px;height:784px;border:1px solid var(--frame);background:var(--white)}
  .layer{position:absolute;left:0;top:0;width:1200px;height:1178px}

  .section-band{position:absolute;z-index:3;height:30px;transform:skewY(-3deg);display:flex;align-items:flex-end;padding-left:6px;padding-right:6px;overflow:visible}
  .section-band.green{background:var(--green)}
  .section-band.orange{background:var(--orange)}
  .section-title{font-family:"Yellowtail",cursive;font-size:23px;line-height:1;color:var(--ink);transform:skewY(3deg);white-space:nowrap;padding-bottom:2px}
  .section-title.long{font-size:17px;letter-spacing:-.3px}
  .section-title.mid{font-size:19px;letter-spacing:-.3px}

  .photo{position:absolute;z-index:1;border-radius:2px}
  .photo.warm{background:linear-gradient(135deg,#b7a083,#d9c7ac 55%,#9c7a58)}
  .photo.greenish{background:linear-gradient(135deg,#7d9a4e,#b8c98b 55%,#6d8a3e)}
  .photo.soup{background:radial-gradient(circle at 45% 50%,#b9852e 0 38%,#e8e4da 40%)}
  .photo.burger{background:linear-gradient(180deg,#c98a45,#e4d3b4 55%,#8b6a3b)}
  .photo.cookie{background:linear-gradient(90deg,#4b3526 0 48%,#d8c29c 52%)}
  .photo.wrap{background:linear-gradient(135deg,#d7c39b,#efe6d3 50%,#a8b88a)}

  .item{position:absolute;z-index:2}
  .item-head{display:flex;align-items:baseline;font-weight:700;font-size:12px;line-height:13px;letter-spacing:.1px}
  .item-name{white-space:nowrap}
  .leader{flex:1;border-bottom:1.6px dotted var(--ink);margin:0 1px 3px}
  .price{white-space:nowrap}
  .item-desc{font-size:8.6px;line-height:10.3px;color:var(--body);margin-top:1px;letter-spacing:-.1px}
  .icons{display:inline-flex;gap:2px;vertical-align:middle;margin-left:4px}
  .icons svg{width:11px;height:11px}

  .legend{position:absolute;left:365px;top:752px;width:216px;height:105px}
  .legend-label{position:absolute;font-family:"Arimo",Arial,sans-serif;font-weight:700;font-size:5px;color:var(--ink);text-align:center;width:50px}

  .caption{position:absolute;left:0;width:1200px;text-align:center;font-family:"Arimo",Arial,sans-serif;font-weight:700}
  .caption.title{top:887px;font-size:30px;color:#111}
  .caption.note{font-size:26px;line-height:32px;color:var(--note)}
</style>
</head>
<body>

<svg width="0" height="0" style="position:absolute" aria-hidden="true">
  <symbol id="i-gf" viewBox="0 0 20 20"><circle cx="10" cy="10" r="8.5" fill="none" stroke="#1d1d1b" stroke-width="1.4"/><path d="M10 4v12M7 7l3 2 3-2M7 10l3 2 3-2" fill="none" stroke="#1d1d1b" stroke-width="1.1"/><path d="M4 4l12 12" stroke="#1d1d1b" stroke-width="1.4"/></symbol>
  <symbol id="i-df" viewBox="0 0 20 20"><circle cx="10" cy="10" r="8.5" fill="none" stroke="#1d1d1b" stroke-width="1.4"/><path d="M7 6h6v9H7zM7 6l1-2h4l1 2" fill="none" stroke="#1d1d1b" stroke-width="1.1"/><path d="M4 4l12 12" stroke="#1d1d1b" stroke-width="1.4"/></symbol>
  <symbol id="i-veg" viewBox="0 0 20 20"><path d="M10 17V9M10 9c-3 0-5-2-5-5 3 0 5 2 5 5zM10 11c2-3 4-4 6-4-1 3-3 4-6 4z" fill="none" stroke="#1d1d1b" stroke-width="1.2"/><path d="M5 17h10" stroke="#1d1d1b" stroke-width="1.2"/></symbol>
  <symbol id="i-vegan" viewBox="0 0 20 20"><path d="M4 16C4 8 9 4 16 4c0 7-4 12-12 12zM4 16l8-8" fill="none" stroke="#1d1d1b" stroke-width="1.2"/></symbol>
  <symbol id="i-nut" viewBox="0 0 20 20"><ellipse cx="7" cy="8" rx="3" ry="4" fill="none" stroke="#1d1d1b" stroke-width="1.1"/><ellipse cx="13" cy="8" rx="3" ry="4" fill="none" stroke="#1d1d1b" stroke-width="1.1"/><ellipse cx="10" cy="14" rx="3" ry="3.5" fill="none" stroke="#1d1d1b" stroke-width="1.1"/></symbol>
</svg>

<div class="spread"></div>

<main class="layer">
  <!-- Section headers -->
  <div class="section-band green" style="left:92px;top:124px;min-width:113px"><span class="section-title">Breakfast</span></div>
  <div class="section-band orange" style="left:342px;top:125px;min-width:116px"><span class="section-title">Bowls</span></div>
  <div class="section-band green" style="left:591px;top:122px;min-width:125px"><span class="section-title">Salad</span></div>
  <div class="section-band orange" style="left:846px;top:131px;min-width:125px"><span class="section-title">Combos</span></div>
  <div class="section-band green" style="left:93px;top:489px;min-width:111px"><span class="section-title">Soups</span></div>
  <div class="section-band green" style="left:346px;top:535px;min-width:113px"><span class="section-title">Wraps</span></div>
  <div class="section-band orange" style="left:100px;top:687px;min-width:126px"><span class="section-title">Smoothies</span></div>
  <div class="section-band orange" style="left:593px;top:499px;min-width:149px"><span class="section-title long">Burgers N' Sammies</span></div>
  <div class="section-band green" style="left:846px;top:317px;min-width:130px"><span class="section-title mid">Snacks N' Sides</span></div>
  <div class="section-band orange" style="left:846px;top:563px;min-width:111px"><span class="section-title">Desserts</span></div>

  <!-- Photo placeholders -->
  <div class="photo warm" role="img" aria-label="Photo of avocado toast topped with tomatoes" style="left:223px;top:106px;width:96px;height:51px"></div>
  <div class="photo warm" role="img" aria-label="Photo of a grain bowl with avocado and grilled chicken" style="left:479px;top:105px;width:91px;height:53px"></div>
  <div class="photo greenish" role="img" aria-label="Photo of a leafy salad with nuts" style="left:732px;top:105px;width:100px;height:50px"></div>
  <div class="photo burger" role="img" aria-label="Photo of a burger with a side salad" style="left:984px;top:103px;width:91px;height:53px"></div>
  <div class="photo warm" role="img" aria-label="Photo of blue corn tortilla chips with guacamole" style="left:984px;top:298px;width:100px;height:48px"></div>
  <div class="photo soup" role="img" aria-label="Photo of a bowl of butternut squash soup" style="left:218px;top:465px;width:101px;height:48px"></div>
  <div class="photo wrap" role="img" aria-label="Photo of a grilled chicken wrap" style="left:497px;top:513px;width:73px;height:56px"></div>
  <div class="photo greenish" role="img" aria-label="Photo of a green smoothie" style="left:247px;top:669px;width:72px;height:44px"></div>
  <div class="photo burger" role="img" aria-label="Photo of a chicken sandwich on a bun" style="left:748px;top:475px;width:77px;height:56px"></div>
  <div class="photo cookie" role="img" aria-label="Photo of chocolate and chocolate chip cookies" style="left:964px;top:537px;width:103px;height:49px"></div>

  <!-- Column 1: Breakfast -->
  <div class="item" style="left:99px;top:161px;width:227px"><div class="item-head"><span class="item-name">PASTRIES</span><span class="leader"></span><span class="price">$0.00</span></div><p class="item-desc">*Croissant (regular, almond, chocolate)<br>Blueberry Muffin Superseed Cookie<span class="icons"><svg><use href="#i-veg"/></svg></span></p></div>
  <div class="item" style="left:99px;top:202px;width:227px"><div class="item-head"><span class="item-name">PARFAIT</span><span class="leader"></span><span class="price">$0.00</span></div><p class="item-desc" style="margin-top:5px">Fresh strawberries and blueberries on yogurt<br>and muesli and topped with honey drizzle.<span class="icons"><svg><use href="#i-veg"/></svg></span></p></div>
  <div class="item" style="left:99px;top:250px;width:227px"><div class="item-head"><span class="item-name">AVACADO SUPER TOAST</span><span class="leader"></span><span class="price">$0.00</span></div><p class="item-desc">Avocado Mash, Tomato, Basil, Ground Flax,HempSeed,<br>Chickpeas, and Moringa Powder on Whole WheatBread.<span class="icons"><svg><use href="#i-vegan"/></svg></span></p></div>
  <div class="item" style="left:99px;top:295px;width:227px"><div class="item-head"><span class="item-name">BRUNCH BURGER</span><span class="leader"></span><span class="price">$0.00</span></div><p class="item-desc">House seasoned beef burger topped with an over<br>medium egg, red leaf lettuce, tomato, housemade<br>pickles and Larder Sauce on a bun.</p></div>
  <div class="item" style="left:99px;top:350px;width:227px"><div class="item-head"><span class="item-name">BREAKFAST SAMMY</span><span class="leader"></span><span class="price">$0.00</span></div><p class="item-desc">Your choice of over medium egg or tofu steak with<br>guacamole, tomato, and Larder sauce on an<br>English muffin.<span style="float:right"><span class="icons"><svg><use href="#i-vegan"/></svg></span>Option*</span></p></div>
  <div class="item" style="left:99px;top:405px;width:227px"><div class="item-head"><span class="item-name">AM BURRITO</span><span class="leader"></span><span class="price">$0.00</span></div><p class="item-desc">Scrambled eggs, onion, red bell pepper, black beans,<br>housemade salsa, yogurt, and pepper<br>jack cheese in a tortilla.<span class="icons"><svg><use href="#i-veg"/></svg></span></p></div>

  <!-- Column 1: Soups -->
  <div class="item" style="left:97px;top:523px;width:227px"><div class="item-head"><span class="item-name">CHICKEN NOODLE</span><span class="leader"></span><span class="price">$0.00</span></div><p class="item-desc">Chicken, egg noodles, root vegetables,<br>oregano &amp; peppercorns.<span class="icons"><svg><use href="#i-df"/></svg></span></p></div>
  <div class="item" style="left:97px;top:568px;width:227px"><div class="item-head"><span class="item-name">LARDER CHILI</span><span class="leader"></span><span class="price">$0.00</span></div><p class="item-desc">Chicken, onions, bell peppers, jalapeños,<br>black &amp; kidney beans, and tomato<span class="icons"><svg><use href="#i-df"/></svg></span></p></div>
  <div class="item" style="left:97px;top:611px;width:227px"><div class="item-head"><span class="item-name">SEASONAL ROTATING</span><span class="leader"></span><span class="price">$0.00</span></div><p class="item-desc">Butternut squash blended with warm spices, and coconut<br>milk.<span style="float:right"><span class="icons"><svg><use href="#i-vegan"/></svg><svg><use href="#i-df"/></svg></span> (Butternut Squash Soup V+, GF)</span></p></div>

  <!-- Column 1: Smoothies -->
  <div class="item" style="left:104px;top:721px;width:227px"><div class="item-head"><span class="item-name">GREEN MACHINE SMOOTHIE</span><span class="leader"></span><span class="price">$0.00</span></div><p class="item-desc">Romaine, spinach, banana, mango, pineapple, flaxmilk,<br>spirulina, almond butter.</p></div>
  <div class="item" style="left:104px;top:775px;width:227px"><div class="item-head"><span class="item-name">ACI SMOOTHIE</span><span class="leader"></span><span class="price">$0.00</span></div><p class="item-desc">Acai, blueberries, banana, pineapple, Macqui<br>berry, flaxmilk, almond butter<span class="icons" style="margin-left:14px"><svg><use href="#i-vegan"/></svg><svg><use href="#i-df"/></svg><svg><use href="#i-nut"/></svg></span></p></div>
  <div class="item" style="left:104px;top:820px;width:227px"><div class="item-head"><span class="item-name">MANGO SMOOTHIE</span><span class="leader"></span><span class="price">$0.00</span></div><p class="item-desc">Mango, flaxmilk, banan, hemp seeds</p></div>

  <!-- Column 2: Bowls -->
  <div class="item" style="left:350px;top:162px;width:226px"><div class="item-head"><span class="item-name">SOUTHWEST BOWL</span><span class="leader"></span><span class="price">$0.00</span></div><p class="item-desc">Your choice of protein with corn, black beans, red<br>onions, almonds and avocado over quinoa<br>with lime hot sauce.<span class="icons" style="margin-left:60px"><svg><use href="#i-df"/></svg><svg><use href="#i-nut"/></svg></span></p></div>
  <div class="item" style="left:350px;top:217px;width:226px"><div class="item-head"><span class="item-name">CHIMI BOWL</span><span class="leader"></span><span class="price">$0.00</span></div><p class="item-desc">Your choice of protein with red bell pepper, mushrooms,<br>zucchini, squash, onion, cherry tomatoes and fresh<br>herb chimichurri on wild and brown rice.<span class="icons" style="margin-left:22px"><svg><use href="#i-df"/></svg></span></p></div>
  <div class="item" style="left:350px;top:272px;width:230px"><div class="item-head"><span class="item-name">SOBA NOODLE BOWL</span><span class="leader"></span><span class="price" style="margin-right:4px">$0.00</span></div><p class="item-desc">Your choice of protein with spinach, snow peas, roasted<br>carrots, red bell pepper, cilantro, sesame seeds and ginger<br>lime sauce over soba noodles.</p></div>
  <div class="item" style="left:350px;top:328px;width:226px"><div class="item-head"><span class="item-name">HOLLYWOOD BOWL</span><span class="leader"></span><span class="price">$0.00</span></div><p class="item-desc">Your choice of protein with broccoli, roasted corn,<br>cherry tomatoes, basil, pepitas, flax seeds and<br>lemon juice on wild and brown rice.<span class="icons" style="margin-left:28px"><svg><use href="#i-df"/></svg></span></p></div>
  <div class="item" style="left:350px;top:383px;width:226px"><div class="item-head"><span class="item-name">LARDER BOWL</span><span class="leader"></span><span class="price">$0.00</span></div><p class="item-desc">Your choice of protein with roasted chickpeas and<br>cauliflower, zesty fennel salad and citrus yogurt.<span class="icons" style="margin-left:8px"><svg><use href="#i-df"/></svg></span></p></div>
  <div class="item" style="left:350px;top:427px;width:226px"><div class="item-head"><span class="item-name">BUDDAH BOWL</span><span class="leader"></span><span class="price">$0.00</span></div><p class="item-desc">Your choice of protein with corn, red kale, sweet potatoes,<br>red cabbage, parsley, oregano, hummus, and farro.</p></div>
  <div class="item" style="left:350px;top:472px;width:226px"><div class="item-head"><span class="item-name">CHILI RICE BOWL</span><span class="leader"></span><span class="price">$0.00</span></div><p class="item-desc">Chicken, onions, bell peppers, jalapeños, black &amp; kidney<br>beans, and tomato over brown rice.</p></div>

  <!-- Column 2: Wraps -->
  <div class="item" style="left:356px;top:574px;width:227px"><div class="item-head"><span class="item-name">RANCHER'S WRAP</span><span class="leader"></span><span class="price">$0.00</span></div><p class="item-desc">Tomato, red onion, hard boiled egg, avocado, feta cheese,<br>microgreens, romaine, grilled chicken and Ranch dressing<br>in a grilled wrap.</p></div>
  <div class="item" style="left:356px;top:630px;width:227px"><div class="item-head"><span class="item-name">VEGAN TUNA WRAP</span><span class="leader"></span><span class="price">$0.00</span></div><p class="item-desc">Vegan tuna, romaine, avocado, celery, shallot, and<br>oregano with Herbalicious Sauce in a<span class="icons" style="margin-left:52px"><svg><use href="#i-vegan"/></svg></span><br>whole grain wrap.</p></div>
  <div class="item" style="left:356px;top:684px;width:227px"><div class="item-head"><span class="item-name">VEGETARIAN WRAP</span><span class="leader"></span><span class="price">$0.00</span></div><p class="item-desc">Roasted chickpeas, romaine, avocado, red bell pepper,<br>shaved carrots, cucumber, spinach,basil, black<br>beans and feta with lemon-hummus in a<span class="icons" style="margin-left:28px"><svg><use href="#i-veg"/></svg></span><br>sprouted 7-grain</p></div>

  <!-- Legend -->
  <svg class="legend" viewBox="0 0 216 105" aria-label="Dietary symbols key">
    <polygon points="0,0 216,3 150,105 28,100" fill="#9bcb3c"/>
    <g transform="translate(27,8)"><use href="#i-gf" width="24" height="24"/></g>
    <g transform="translate(86,8)"><use href="#i-df" width="24" height="24"/></g>
    <g transform="translate(140,8)"><use href="#i-veg" width="24" height="24"/></g>
    <g transform="translate(63,54)"><use href="#i-vegan" width="24" height="24"/></g>
    <g transform="translate(112,54)"><use href="#i-nut" width="24" height="24"/></g>
  </svg>
  <span class="legend-label" style="left:389px;top:792px">GLUTEN-FREE</span>
  <span class="legend-label" style="left:448px;top:792px">DAIRY-FREE</span>
  <span class="legend-label" style="left:502px;top:792px">VEGETARIAN</span>
  <span class="legend-label" style="left:410px;top:836px">VEGAN</span>
  <span class="legend-label" style="left:462px;top:836px">CONTAINS NUTS</span>

  <!-- Column 3: Salad -->
  <div class="item" style="left:596px;top:157px;width:227px"><div class="item-head"><span class="item-name">AVOCADO, GOLDEN BEET</span></div><div class="item-head"><span class="item-name">&amp; CRANBERRY SALAD</span><span class="leader"></span><span class="price">$0.00</span></div><p class="item-desc">Gold beets, avocado, dried cranberries, watermelon radish,<br>red kale, romaine, mixed greens, and pepitas<br>served with Golden Buddha dressing.<span class="icons" style="margin-left:36px"><svg><use href="#i-veg"/></svg><svg><use href="#i-df"/></svg></span></p></div>
  <div class="item" style="left:596px;top:223px;width:227px"><div class="item-head"><span class="item-name">BURRATA SALAD</span><span class="leader"></span><span class="price">$0.00</span></div><p class="item-desc">Tomato, melon, shredded basil, balsamic glaze, fresh<br>cracked pepper, and olive oil with burrata.<span class="icons" style="margin-left:18px"><svg><use href="#i-veg"/></svg><svg><use href="#i-df"/></svg></span></p></div>
  <div class="item" style="left:596px;top:279px;width:227px"><div class="item-head"><span class="item-name">MEDITERRANEAN SALAD</span><span class="leader"></span><span class="price">$0.00</span></div><p class="item-desc">Cucumbers, Kalamata olives, cherry tomatoes, parsley,<br>tricolor quinoa, hard-boiled egg, and hummus on mixed<br>greens, romaine, and red cabbage with<br>lemon-olive oil dressing.<span class="icons" style="margin-left:60px"><svg><use href="#i-veg"/></svg><svg><use href="#i-df"/></svg></span></p></div>
  <div class="item" style="left:596px;top:344px;width:227px"><div class="item-head"><span class="item-name">VEGAN CHEF SALAD</span><span class="leader"></span><span class="price">$0.00</span></div><p class="item-desc">Roasted potatoes and carrots, chickpeas, avocado,<br>microgreens and walnuts on mixed greens, romaine, and<br>red kale with vegan ranch.<span class="icons" style="margin-left:26px"><svg><use href="#i-vegan"/></svg><svg><use href="#i-df"/></svg><svg><use href="#i-nut"/></svg></span></p></div>
  <div class="item" style="left:596px;top:408px;width:227px"><div class="item-head"><span class="item-name">RANCHER'S SALAD</span><span class="leader"></span><span class="price">$0.00</span></div><p class="item-desc">Tomato, red onion, hard boiled egg, avocado, feta<br>cheese, microgreens, and grilled chicken on<br>romaine with Ranch dressing.<span class="icons" style="margin-left:56px"><svg><use href="#i-veg"/></svg><svg><use href="#i-df"/></svg></span></p></div>

  <!-- Column 3: Burgers -->
  <div class="item" style="left:598px;top:537px;width:227px"><div class="item-head"><span class="item-name">AIR FRIED CHICKEN SAMMY</span><span class="leader"></span><span class="price">$0.00</span></div><p class="item-desc">Air fried chicken breast topped with red leaf lettuce, tomato,<br>house made pickles and Larder Sauce on a bun served<br>with choice of salad of fries.</p></div>
  <div class="item" style="left:598px;top:592px;width:227px"><div class="item-head"><span class="item-name">GRILLED CHICKEN SAMMY</span><span class="leader"></span><span class="price">$0.00</span></div><p class="item-desc">Grilled chicken topped with guacamole, red leaf lettuce,<br>tomato, house made pickles and Larder Sauce. Served<br>with regular fries or side salad.</p></div>
  <div class="item" style="left:598px;top:647px;width:227px"><div class="item-head"><span class="item-name">CLASSIC BEEF BURGER</span><span class="leader"></span><span class="price">$0.00</span></div><p class="item-desc">House seasoned beef burger topped with red leaf lettuce,<br>tomato, cheddar cheese, house made pickles and Larder<br>Sauce on a bun served with choice of salad of fries.</p></div>
  <div class="item" style="left:598px;top:702px;width:227px"><div class="item-head"><span class="item-name">BLACK BEAN PINE</span></div><div class="item-head"><span class="item-name">NUT BURGER</span><span class="leader"></span><span class="price">$0.00</span></div><p class="item-desc">House made black bean pine nut burger topped with red<br>leaf lettuce, tomato, house made pickles and mustard aioli<br>on a bun served with choice of salad of fries.<span class="icons"><svg><use href="#i-vegan"/></svg><svg><use href="#i-nut"/></svg></span></p></div>
  <div class="item" style="left:598px;top:781px;width:227px"><div class="item-head"><span class="item-name">SALMON BURGER</span><span class="leader"></span><span class="price">$0.00</span></div><p class="item-desc">House made salmon burger topped with red leaf lettuce,<br>tomato, house made pickles and Larder yogurt on a bun<br>served with choice of salad of fries.</p></div>

  <!-- Column 4: Combos -->
  <div class="item" style="left:849px;top:164px;width:227px"><div class="item-head"><span class="item-name">SOUP + SALAD</span><span class="leader"></span><span class="price">$0.00</span></div><p class="item-desc">"Your choice of soup and side salad.<br>16oz soup + 38oz salad"</p></div>
  <div class="item" style="left:849px;top:209px;width:227px"><div class="item-head"><span class="item-name">AVO TOAST COMBO</span><span class="leader"></span><span class="price">$0.00</span></div><p class="item-desc">Half avocado toast and your choice of soup. 16oz</p></div>
  <div class="item" style="left:849px;top:243px;width:227px"><div class="item-head"><span class="item-name">SOUP + SAMMY</span><span class="leader"></span><span class="price">$0.00</span></div><p class="item-desc">"Your choice of soup and sandwich.<br>16oz soup + Sandwich"</p></div>

  <!-- Column 4: Snacks -->
  <div class="item" style="left:849px;top:353px;width:227px"><div class="item-head"><span class="item-name">FRIES</span><span class="leader"></span><span class="price">$0.00</span></div><p class="item-desc">Hand cut air-fries with house seasonings.<br>Choose regular or sweet potato fries.<span class="icons" style="margin-left:20px"><svg><use href="#i-vegan"/></svg><svg><use href="#i-df"/></svg></span></p></div>
  <div class="item" style="left:849px;top:408px;width:227px"><div class="item-head"><span class="item-name">SIDE SALAD</span><span class="leader"></span><span class="price">$0.00</span></div><p class="item-desc">Your choice of House, Golden Beet,<br>Mediterranean, or Vegan Chef side salad. (24oz)</p></div>
  <div class="item" style="left:849px;top:453px;width:227px"><div class="item-head"><span class="item-name">GUAC + CHIPS</span><span class="leader"></span><span class="price">$0.00</span></div><p class="item-desc">Guacamole with blue corn tortilla chips.<span class="icons" style="margin-left:8px"><svg><use href="#i-vegan"/></svg><svg><use href="#i-df"/></svg></span></p></div>
  <div class="item" style="left:849px;top:498px;width:227px"><div class="item-head"><span class="item-name">HUMMUS + CHIPS</span><span class="leader"></span><span class="price">$0.00</span></div><p class="item-desc">Hummus with blue corn tortilla chips.</p></div>

  <!-- Column 4: Desserts -->
  <div class="item" style="left:851px;top:600px;width:227px"><div class="item-head"><span class="item-name">DATE COFFEE CAKE</span><span class="leader"></span><span class="price">$0.00</span></div><p class="item-desc">Signature date coffee cake with walnuts.<span class="icons" style="margin-left:5px"><svg><use href="#i-vegan"/></svg><svg><use href="#i-nut"/></svg></span></p></div>
  <div class="item" style="left:851px;top:645px;width:227px"><div class="item-head"><span class="item-name">FRUIT + SPICES</span><span class="leader"></span><span class="price">$0.00</span></div><p class="item-desc">Strawberry, pineapple, green apple, orange,<br>and blueberries with lime and chili seasoning.<span class="icons" style="margin-left:6px"><svg><use href="#i-vegan"/></svg><svg><use href="#i-df"/></svg></span></p></div>
  <div class="item" style="left:851px;top:700px;width:227px"><div class="item-head"><span class="item-name">COOKIES</span><span class="leader"></span><span class="price">$0.00</span></div><p class="item-desc">Your choice of Chocolate Chip or Double<br>Chocolate Chip fresh baked cookie.<span class="icons" style="margin-left:28px"><svg><use href="#i-veg"/></svg></span></p></div>
  <div class="item" style="left:851px;top:755px;width:227px"><div class="item-head"><span class="item-name">LARDER CHOCOLATE</span></div><div class="item-head"><span class="item-name">MOUSSE</span><span class="leader"></span><span class="price">$0.00</span></div><p class="item-desc">Served with grated dark chocolate.<span class="icons" style="margin-left:6px"><svg><use href="#i-vegan"/></svg><svg><use href="#i-df"/></svg></span></p></div>
</main>

<p class="caption title">inside of brochure</p>
<p class="caption note" style="top:953px">NOTE...I have used photos from your web page and these will<br>need to be upgraded to the original photos for print.</p>
<p class="caption note" style="top:1048px">Please give me feedback and<br>would be glad to make any changes you need.</p>

</body>
</html>
```